Notary Signing Agent Need Business card Design

Need a Business card design for my new company. RT Belvoni-Strand LLC
Mobile Notary Signing Agent. I go to the customer for closing of Mortgage's Documents . possible signs of honesty, integrity and confidentiality.

Work with Title company to Notary Mortgage closing.

My Target Market is Title companies. Banks and Financial Institution.

Color Blue to Black Professional ) if needed some Green Little Red

And possible a company logo.

Mobile ( travel to clients ) Integrity, Honest Trustworthy. A show of Professional services.

Would like company name and my name on card

Use both sides and front with business name and my name. phone numbers.

Target Market(s)

Title company, Banks mortgage company

Industry/Entity Type

Travel

Contact Information for Business Card

Notary, Certified signing agent, Mobile

Colors
0455a3

Requirements
Must have
• Name of company , owners name phone number,
Nice to have
• blue and black color like a professional look but not limit to these only.
• a stand out from other cards .

```html
<!DOCTYPE html>
<html lang="en">
<head>
<meta charset="utf-8">
<title>RT Belvoni-Strand LLC – Business Card</title>
<link rel="stylesheet" href="https://fonts.googleapis.com/css2?family=Arimo:wght@400;700&display=swap">
<style>
  :root {
    --stage: #6a6a6a;
    --brand-blue: #0455a3;
    --blue-light: #1a74c8;
    --blue-deep: #023f82;
    --card-black: #1d1d1d;
    --text-white: #ffffff;
    --text-soft: #e6e6e6;
    --rule-grey: #8a8a8a;
  }
  html, body {
    margin: 0;
    width: 1200px;
    height: 1200px;
    overflow: hidden;
    background: var(--stage);
    font-family: "Arimo", Arial, sans-serif;
  }
  .canvas {
    position: relative;
    width: 1200px;
    height: 1200px;
  }
  .card {
    position: absolute;
    left: 250px;
    width: 700px;
    height: 400px;
    overflow: hidden;
    box-shadow: 0 6px 18px rgba(0,0,0,0.25);
  }
  /* Front */
  .card-front {
    top: 150px;
    background: radial-gradient(circle at 30% 45%, var(--blue-light) 0%, var(--brand-blue) 45%, var(--blue-deep) 100%);
  }
  .front-company {
    position: absolute;
    left: 48px;
    bottom: 52px;
    margin: 0;
    color: var(--text-white);
    font-weight: 700;
    font-size: 34px;
    letter-spacing: 1px;
    text-transform: uppercase;
  }
  /* Back */
  .card-back {
    top: 650px;
    background: var(--card-black);
  }
  .back-art {
    position: absolute;
    inset: 0;
  }
  .back-company {
    position: absolute;
    left: 150px;
    top: 52px;
    margin: 0;
    color: var(--blue-light);
    font-weight: 700;
    font-size: 26px;
    letter-spacing: 1px;
    text-transform: uppercase;
  }
  .owner {
    position: absolute;
    right: 345px;
    top: 168px;
    text-align: right;
  }
  .owner-name {
    margin: 0;
    color: var(--blue-light);
    font-weight: 700;
    font-size: 22px;
    text-transform: uppercase;
  }
  .owner-title {
    margin: 4px 0 0;
    color: var(--text-white);
    font-weight: 700;
    font-size: 12px;
    letter-spacing: 1px;
    text-transform: uppercase;
  }
  .divider {
    position: absolute;
    left: 372px;
    top: 152px;
    width: 1px;
    height: 100px;
    background: var(--rule-grey);
  }
  .contact-list {
    position: absolute;
    left: 392px;
    top: 158px;
    margin: 0;
    padding: 0;
    list-style: none;
  }
  .contact-item {
    display: flex;
    align-items: center;
    gap: 12px;
    height: 30px;
    color: var(--text-soft);
    font-size: 17px;
  }
  .contact-icon {
    width: 16px;
    height: 16px;
    fill: var(--blue-light);
  }
  .web-address {
    position: absolute;
    left: 0;
    right: 0;
    bottom: 6px;
    margin: 0;
    text-align: center;
    color: var(--text-white);
    font-size: 15px;
    font-weight: 700;
  }
</style>
</head>
<body>
<main class="canvas">
  <section class="card card-front" aria-label="Card front">
    <h1 class="front-company">RT Belvoni-Strand LLC.</h1>
  </section>

  <section class="card card-back" aria-label="Card back">
    <svg class="back-art" width="700" height="400" viewBox="0 0 700 400" aria-hidden="true">
      <defs>
        <linearGradient id="bandBlue" x1="0" y1="0" x2="1" y2="0">
          <stop offset="0" stop-color="#023f82"/>
          <stop offset="0.5" stop-color="#0a62b8"/>
          <stop offset="1" stop-color="#023f82"/>
        </linearGradient>
      </defs>
      <path d="M0 350 Q350 290 700 350" fill="none" stroke="#cfcfcf" stroke-width="3"/>
      <path d="M0 362 Q350 304 700 362 L700 400 L0 400 Z" fill="url(#bandBlue)"/>
    </svg>

    <h2 class="back-company">RT Belvoni-Strand LLC.</h2>

    <div class="owner">
      <p class="owner-name">Daniel R Hale</p>
      <p class="owner-title">Owner</p>
    </div>

    <div class="divider"></div>

    <ul class="contact-list">
      <li class="contact-item">
        <svg class="contact-icon" viewBox="0 0 16 16" aria-hidden="true"><path d="M3 1l3 3-1.5 2a9 9 0 0 0 5.5 5.5L12 10l3 3-2 2C6 15 1 10 1 3z"/></svg>
        555-214-3390
      </li>
      <li class="contact-item">
        <svg class="contact-icon" viewBox="0 0 16 16" aria-hidden="true"><rect x="4" y="1" width="8" height="14" rx="1.5"/><rect x="5.5" y="3" width="5" height="8" fill="#1d1d1d"/></svg>
        555-618-2047
      </li>
      <li class="contact-item">
        <svg class="contact-icon" viewBox="0 0 16 16" aria-hidden="true"><rect x="1" y="3" width="14" height="10" rx="1"/><path d="M1.5 4l6.5 5 6.5-5" fill="none" stroke="#1d1d1d" stroke-width="1.3"/></svg>
        email@mail.com
      </li>
    </ul>

    <p class="web-address">www.website.com</p>
  </section>
</main>
</body>
</html>
```